Professional Website

We are looking for a new website for our Staffing Company. Attached is a document with all the details and pages needed along with some examples of others websites.

We want a professional Look and feel around the same color theme as the attached Vivid Vision.

We currently host our site on SiteKarn.io. If the winning designer can also add to SiteKarn, that is a plus.

```html
<!DOCTYPE html>
<html lang="en">
<head>
<meta charset="utf-8">
<title>HireRidge Inc – Recruiting Agency</title>
<link rel="stylesheet" href="https://fonts.googleapis.com/css2?family=Poppins:wght@400;500;600;700;800&display=swap">
<style>
:root{
  --blue:#2a4fb0;
  --ink:#1c1c1c;
  --muted:#666;
  --band:#ececec;
  --footer:#1f1f1f;
  --white:#fff;
}
*{box-sizing:border-box;margin:0;padding:0}
html,body{width:849px;height:1200px;overflow:hidden;background:var(--white)}
body{font-family:'Poppins',sans-serif;color:var(--ink);position:relative}

.site-header{position:absolute;top:0;left:0;width:849px;height:88px;background:var(--white)}
.brand{position:absolute;left:70px;top:24px;display:flex;align-items:center;gap:10px}
.brand-square{width:24px;height:24px;background:var(--blue)}
.brand-name{font-weight:800;font-size:32px;color:var(--blue);letter-spacing:-0.5px;line-height:1}
.portal-links{position:absolute;top:12px;left:352px;display:flex;gap:6px}
.portal-btn{font-size:9px;font-weight:500;color:var(--blue);border:1px solid #c9d3ec;border-radius:3px;padding:4px 8px;white-space:nowrap}
.hotline{position:absolute;top:10px;left:672px;display:flex;align-items:center;gap:6px}
.hotline-icon{width:22px;height:22px;border-radius:50%;background:var(--blue);display:flex;align-items:center;justify-content:center;flex:none}
.hotline-text{font-size:9px;line-height:1.25;color:var(--ink);white-space:nowrap}
.hotline-text b{display:block;font-weight:600}
.main-nav{position:absolute;top:46px;left:340px;display:flex;align-items:center;font-size:10px;font-weight:500}
.main-nav a{color:var(--ink);text-decoration:none;padding:6px 16px;border-right:1px solid #bbb;white-space:nowrap}
.main-nav a:last-child{border-right:none;padding-right:0}
.main-nav a.active{background:var(--blue);color:var(--white);border-radius:3px;border-right:none;margin-right:4px}

.hero{position:absolute;top:88px;left:0;width:849px;height:267px;overflow:hidden}
.hero-globe{position:absolute;left:113px;top:110px;width:610px;height:200px;border-radius:305px 305px 0 0;background:radial-gradient(ellipse at 50% 100%,#e3e8f4 0%,#eef1f8 55%,#fafbfd 100%)}
.hero-title{position:relative;text-align:center;font-size:29px;font-weight:700;line-height:1.35;padding-top:30px}

.choices{position:absolute;top:355px;left:0;width:849px;height:300px;background:var(--band)}
.choice-card{position:absolute;top:0;width:354px;height:300px;background:var(--white);box-shadow:0 3px 12px rgba(0,0,0,.12);text-align:center}
.choice-card.seeker{left:70px}
.choice-card.employer{left:425px;box-shadow:0 3px 12px rgba(0,0,0,.12),-1px 0 0 #ddd}
.choice-title{font-size:21px;font-weight:600;margin-top:22px}
.choice-sub{font-size:8.5px;color:var(--muted);margin-top:4px}
.choice-link{display:inline-block;margin-top:6px;font-size:10.5px;font-weight:500;color:var(--blue);text-decoration:none}
.choice-photo{position:absolute;left:0;bottom:0;width:100%;height:195px}
.seeker .choice-photo{background:linear-gradient(135deg,#d8d2cc,#8a7f78 60%,#3a3a40)}
.employer .choice-photo{background:linear-gradient(135deg,#f2f2f2,#b83a36 55%,#3b3b3b)}

.about{position:absolute;top:655px;left:0;width:849px;height:280px}
.about-title{position:absolute;left:70px;top:92px;font-size:26px;font-weight:700}
.about-text{position:absolute;left:70px;top:138px;width:400px;font-size:9.5px;line-height:1.75;color:#444}
.about-photo{position:absolute;left:470px;top:20px;width:310px;height:260px;background:radial-gradient(ellipse at 50% 60%,#c9a48c 0%,#8a6a5a 40%,#fff 72%)}
.about-quote{position:absolute;left:650px;top:58px;width:130px;font-size:9px;font-weight:500;line-height:1.35;color:var(--ink);text-align:right}

.site-footer{position:absolute;top:935px;left:0;width:849px;height:265px;background:var(--footer);color:var(--white)}
.footer-brand{position:absolute;left:70px;top:112px;display:flex;align-items:center;gap:10px}
.footer-brand .brand-square{background:var(--white)}
.footer-brand .brand-name{color:var(--white);font-size:36px}
.areas{position:absolute;left:433px;top:45px}
.areas h4{font-size:11px;font-weight:600;margin-bottom:8px}
.areas li{list-style:none;font-size:9.5px;line-height:1.9;color:#ccc}
.footer-hotline{position:absolute;left:600px;top:120px;display:flex;align-items:center;gap:14px}
.footer-hotline .hotline-icon{width:34px;height:34px}
.footer-hotline-label{font-size:11px;font-weight:600}
.footer-hotline-number{font-size:19px;font-weight:500}
.footer-rule{position:absolute;left:70px;right:70px;top:210px;height:1px;background:#444}
.copyright{position:absolute;left:0;width:100%;top:232px;text-align:center;font-size:10px;color:#bbb}
</style>
</head>
<body>
<header class="site-header">
  <div class="brand"><span class="brand-square"></span><span class="brand-name">HireRidge</span></div>
  <div class="portal-links">
    <span class="portal-btn">Employee Login</span>
    <span class="portal-btn">PayTile Card Login</span>
    <span class="portal-btn">ShiftDesk Login</span>
  </div>
  <div class="hotline">
    <span class="hotline-icon"><svg width="11" height="11" viewBox="0 0 24 24"><path fill="#fff" d="M6.6 10.8a15 15 0 0 0 6.6 6.6l2.2-2.2a1 1 0 0 1 1-.25 11.4 11.4 0 0 0 3.6.57 1 1 0 0 1 1 1V20a1 1 0 0 1-1 1A17 17 0 0 1 3 4a1 1 0 0 1 1-1h3.5a1 1 0 0 1 1 1c0 1.25.2 2.45.57 3.57a1 1 0 0 1-.25 1z"/></svg></span>
    <span class="hotline-text"><b>Hotline</b># 555-210-4400</span>
  </div>
  <nav class="main-nav">
    <a class="active" href="#">HOME</a>
    <a href="#">ABOUT</a>
    <a href="#">JOB ⌄</a>
    <a href="#">OFFICE INFO</a>
    <a href="#">CONTACT US</a>
  </nav>
</header>

<section class="hero">
  <div class="hero-globe" role="img" aria-label="Faded world globe with connection points"></div>
  <h1 class="hero-title">Recruiting Agency For Temporary<br>And Direct Hire Employees</h1>
</section>

<section class="choices">
  <article class="choice-card seeker">
    <h2 class="choice-title">I'm looking for a Job</h2>
    <p class="choice-sub">Browse open roles across clerical and industrial teams</p>
    <a class="choice-link" href="#">Contact Us Today ⟶</a>
    <div class="choice-photo" role="img" aria-label="Photo of job seekers working together at a laptop"></div>
  </article>
  <article class="choice-card employer">
    <h2 class="choice-title">I need Employees</h2>
    <p class="choice-sub">Find reliable staff for short or long term needs</p>
    <a class="choice-link" href="#">Contact Us Today ⟶</a>
    <div class="choice-photo" role="img" aria-label="Photo of a business meeting on red sofas"></div>
  </article>
</section>

<section class="about">
  <div class="about-photo" role="img" aria-label="Photo of a smiling woman who found a job"></div>
  <p class="about-quote">"HireRidge helped me land my dream job!"</p>
  <h2 class="about-title">HireRidge Inc</h2>
  <p class="about-text">The best part of our daily work is that we are always bringing people together. Our clients come to us in search of the right candidate, and job seekers reach us when they need a new role. Being able to match both sides and connect them is truly rewarding. It is a reminder that in today's market, employers compete for top talent. That keeps us growing.</p>
</section>

<footer class="site-footer">
  <div class="footer-brand"><span class="brand-square"></span><span class="brand-name">HireRidge</span></div>
  <div class="areas">
    <h4>Areas we serve</h4>
    <ul><li>North Valley</li><li>Cedar Park</li><li>Lakeside</li></ul>
  </div>
  <div class="footer-hotline">
    <span class="hotline-icon"><svg width="16" height="16" viewBox="0 0 24 24"><path fill="#fff" d="M6.6 10.8a15 15 0 0 0 6.6 6.6l2.2-2.2a1 1 0 0 1 1-.25 11.4 11.4 0 0 0 3.6.57 1 1 0 0 1 1 1V20a1 1 0 0 1-1 1A17 17 0 0 1 3 4a1 1 0 0 1 1-1h3.5a1 1 0 0 1 1 1c0 1.25.2 2.450.57 3.57a1 1 0 0 1-.25 1z"/></svg></span>
    <div><div class="footer-hotline-label">Hotline</div><div class="footer-hotline-number"># 555-210-4400</div></div>
  </div>
  <div class="footer-rule"></div>
  <p class="copyright">©Copyright 2023 HireRidge Inc. All Rights Reserved.</p>
</footer>
</body>
</html>
```